Business card design needed

I have a leadership coaching and consultancy business which specialises in the education sector. I would like a clean, professional design). The design needs to speak to strength, support, new learning, connections & a growth mindest.

I am also looking for a unique LOGO. This is very important.

Target Market(s)

Educational Leaders & executives

Industry/Entity Type

Leadership

Contact Information for Business Card

Miranda Voss
Principal Coach & Consultant
Miranda Voss Coaching & Consulting
0491 362 815
miranda.voss@quillmail.example
I also would like my facebook, twitter and linkedin accounts to appear

Logo styles of interest
Lettermark Logo
Requirements
Must have
• A 2 sided business card with contact details on the back
A logo

```html
<!DOCTYPE html>
<html lang="en">
<head>
<meta charset="utf-8">
<title>Miranda Voss Coaching &amp; Consulting – Business Card</title>
<link rel="stylesheet" href="https://fonts.googleapis.com/css2?family=League+Gothic&family=Open+Sans:wght@400&display=swap">
<style>
  :root {
    --brand-yellow: #ffcd05;
    --ink-grey: #58595b;
    --name-grey: #6d6e71;
    --bar-grey: #5b5b5b;
    --card-white: #ffffff;
    --text-white: #ffffff;
  }
  * { margin: 0; padding: 0; box-sizing: border-box; }
  html, body {
    width: 1200px;
    height: 693px;
    overflow: hidden;
  }
  body {
    position: relative;
    background: var(--brand-yellow);
    font-family: "Open Sans", Arial, sans-serif;
  }
  .card {
    position: absolute;
    left: 79px;
    top: 166px;
    width: 1039px;
    height: 333px;
    background: var(--card-white);
  }
  .display {
    position: absolute;
    font-family: "League Gothic", "Arial Narrow", sans-serif;
    font-weight: 400;
    line-height: 1;
    white-space: nowrap;
    text-transform: uppercase;
  }
  .contact-name {
    right: 530px;
    top: 38px;
    font-size: 88px;
    color: var(--name-grey);
    transform: scaleX(0.74);
    transform-origin: right top;
  }
  .contact-name .surname { color: var(--brand-yellow); }
  .brand-name {
    left: 519px;
    top: 90px;
    font-size: 138px;
    color: var(--brand-yellow);
    transform: scaleX(0.72);
    transform-origin: left top;
  }
  .brand-tagline {
    left: 519px;
    top: 218px;
    font-size: 92px;
    color: var(--ink-grey);
    transform: scaleX(0.74);
    transform-origin: left top;
  }
  .info-bar {
    position: absolute;
    left: 0;
    width: 444px;
    height: 48px;
    background: var(--bar-grey);
    color: var(--text-white);
    font-size: 22px;
    line-height: 48px;
    text-align: right;
    padding-right: 10px;
    white-space: nowrap;
  }
  .info-bar.phone { top: 125px; }
  .info-bar.email { top: 177px; font-size: 21px; }
  .icon-tile {
    position: absolute;
    width: 51px;
    height: 48px;
    background: var(--bar-grey);
    display: flex;
    align-items: center;
    justify-content: center;
  }
  .icon-tile.phone-icon { left: 448px; top: 125px; }
  .icon-tile.email-icon { left: 448px; top: 177px; }
  .social-tile { top: 230px; }
  .social-tile.first { left: 342px; }
  .social-tile.second { left: 395px; }
  .social-tile.third { left: 448px; }
</style>
</head>
<body>
  <div class="card">
    <div class="display contact-name">Miranda <span class="surname">Voss</span></div>

    <div class="info-bar phone">0491 362 815</div>
    <div class="icon-tile phone-icon">
      <svg width="26" height="32" viewBox="0 0 26 32" aria-hidden="true">
        <path d="M6 2 L11 2 L12 9 L9 11 Q11 19 16 23 L19 21 L24 25 L22 30 Q14 31 8 22 Q3 13 6 2 Z"
              fill="none" stroke="#ffffff" stroke-width="2" stroke-linejoin="round"/>
      </svg>
    </div>

    <div class="info-bar email">miranda.voss@quillmail.example</div>
    <div class="icon-tile email-icon">
      <svg width="30" height="22" viewBox="0 0 30 22" aria-hidden="true">
        <rect x="1" y="1" width="28" height="20" fill="none" stroke="#ffffff" stroke-width="2"/>
        <path d="M1 1 L15 13 L29 1 M1 21 L11 10 M29 21 L19 10" fill="none" stroke="#ffffff" stroke-width="2"/>
      </svg>
    </div>

    <div class="icon-tile social-tile first" aria-label="Professional network profile"></div>
    <div class="icon-tile social-tile second" aria-label="Microblog profile"></div>
    <div class="icon-tile social-tile third" aria-label="Social network profile"></div>

    <div class="display brand-name">Miranda Voss</div>
    <div class="display brand-tagline">Coaching &amp; Consulting</div>
  </div>
</body>
</html>
```